Webdesign Kornbach 31
Zielgruppe
Beratung zu Treppenliften
Aufgabenstellung
Im Wesentlichen wird das Layout für die Startseite gesucht (Landingpage).
Inhaltsseiten sollten aber gedanklich berücksichtigt werden.
Die Detailierte Beschreibung finden Sie in den PDF der Anlagen.
Bitte unbedingt diese Dokumente beachten!
--- Allgemein
Ich (der Auftraggeber) bin Betreiber einer kleinen Webseiten-Agentur und suche nach neuen Wegen um an umsetzbare und ansprechende und dennoch individuell auf den Kunden abgestimmte Layoutvorschläge zu kommen.
Die Programmierung wird auf jeden Fall von mir durchgeführt.

```html
<!DOCTYPE html>
<html lang="de">
<head>
<meta charset="utf-8">
<title>Kornbach 31 – Treppenlift Beratung</title>
<link href="https://fonts.googleapis.com/css2?family=Fira+Sans:wght@400;500;600;700&family=Caveat&display=swap" rel="stylesheet">
<style>
:root{
  --blue:#0063b4;
  --blue-dark:#0a57a0;
  --ink:#222;
  --text:#333;
  --grey-bg:#f6f6f6;
  --line:#d9d9d9;
  --white:#fff;
}
*{box-sizing:border-box;margin:0;padding:0}
html,body{width:1200px;height:2634px;overflow:hidden}
body{font-family:"Fira Sans",sans-serif;color:var(--text);background:var(--white);position:relative}

/* header */
.site-header{position:absolute;left:0;top:0;width:1200px;height:128px;border-bottom:3px solid var(--blue);background:var(--white)}
.topbar{position:absolute;left:600px;top:0;width:600px;height:42px;background:var(--grey-bg);font-size:12px;color:var(--ink);display:flex;align-items:center;gap:30px;padding-left:105px}
.topbar span{display:flex;align-items:center;gap:8px}
.brand{position:absolute;left:90px;top:36px;display:flex;align-items:center;gap:12px;font-size:28px;font-weight:600;color:var(--blue)}
.brand i{width:32px;height:32px;border-radius:50%;background:var(--blue);display:block}
.main-nav{position:absolute;left:600px;top:68px;display:flex;align-items:center;font-size:13px;font-weight:500;color:var(--ink)}
.main-nav a{color:inherit;text-decoration:none;margin-right:45px}
.main-nav a:nth-child(2){margin-right:40px}
.main-nav .btn-contact{background:var(--blue);color:var(--white);border-radius:20px;padding:11px 23px;margin-left:-12px}

/* hero */
.hero{position:absolute;left:0;top:128px;width:1200px;height:407px;background:linear-gradient(90deg,#f1f1f0 0%,#e9e8e6 40%,#dedcd8 70%,#d4d4d6 100%)}
.hero-title{position:absolute;left:100px;top:123px;font-size:45px;line-height:50px;font-weight:700;color:var(--blue)}
.hero-sub{position:absolute;left:100px;top:284px;font-family:"Caveat",cursive;font-size:25px;line-height:27px;color:var(--ink)}
.hero-arrow{position:absolute;left:428px;top:300px}

.cta-band{position:absolute;left:0;top:535px;width:1200px;height:111px;background:var(--blue);color:var(--white);text-align:center;padding-top:28px}
.cta-band h2{font-size:26px;font-weight:600;line-height:30px}
.cta-band p{font-size:21px;font-weight:500}

/* lift types */
.lift-types{position:absolute;left:0;top:646px;width:1200px;height:448px;background:var(--grey-bg)}
.lift-types h2{position:absolute;top:62px;width:100%;text-align:center;font-size:35px;font-weight:500;color:var(--blue)}
.lift-card{position:absolute;top:143px;width:240px;height:179px;background:var(--white);border-radius:6px;box-shadow:0 2px 10px rgba(0,0,0,.05);text-align:center}
.lift-card .icon{width:94px;height:94px;margin:28px auto 0;border-radius:50%;background:#f3f4f6;display:flex;align-items:center;justify-content:center}
.lift-card .label{margin-top:8px;font-size:19px;font-weight:500;color:var(--ink)}
.lift-card.is-active{background:var(--blue)}
.lift-card.is-active .icon{background:#1a73c0}
.lift-card.is-active .label{color:var(--white)}
.slider-bars{position:absolute;top:372px;left:415px;display:flex;gap:15px}
.slider-bars i{width:41px;height:4px;background:#d6d6d6;display:block;border-radius:2px}
.slider-bars i.on{background:var(--blue)}

/* about */
.about-brand{position:absolute;top:1180px;width:1200px;display:flex;justify-content:center;align-items:center;gap:12px;font-size:28px;font-weight:600;color:var(--blue)}
.about-brand i{width:32px;height:32px;border-radius:50%;background:var(--blue);display:block}
.about-col{position:absolute;top:1302px;width:330px;font-size:13.4px;line-height:22px;color:var(--text)}
.about-col p+p{margin-top:22px}

/* feature grid */
.photo{position:absolute}
.feature-box{position:absolute;width:300px;height:300px;background:var(--blue);color:var(--white);padding:58px 40px 0 45px}
.feature-box h3{font-size:18px;font-weight:500;line-height:22px;margin-bottom:22px}
.feature-box p{font-size:13.5px;line-height:22px}

/* partners */
.partners{position:absolute;top:2290px;left:0;width:1200px;display:flex;justify-content:space-around;padding:0 80px;font-size:22px;font-weight:600;color:#8a8a8a}
.partners span{display:flex;align-items:center;gap:8px}
.partners span i{width:18px;height:18px;border-radius:50%;background:#9a9a9a;display:block}
.partner-dots{position:absolute;top:2386px;left:570px;display:flex;gap:9px}
.partner-dots i{width:14px;height:14px;border-radius:50%;border:1.5px solid var(--blue);display:block}
.partner-dots i.on{background:radial-gradient(circle,var(--blue) 0 3.5px,var(--white) 4px)}

/* footer */
.footer-contact{position:absolute;left:0;top:2460px;width:1200px;height:128px;background:var(--grey-bg);display:flex;justify-content:center;align-items:center;gap:46px;font-size:13.5px;color:var(--ink)}
.footer-contact span{display:flex;align-items:center;gap:9px}
.footer-bar{position:absolute;left:0;top:2588px;width:1200px;height:46px;background:var(--blue);color:var(--white);font-size:12px}
.footer-bar .copy{position:absolute;left:88px;top:16px;font-weight:600}
.footer-bar .legal{position:absolute;right:89px;top:16px;display:flex;gap:44px}
</style>
</head>
<body>

<header class="site-header">
  <div class="topbar">
    <span><svg width="16" height="16" viewBox="0 0 24 24" fill="none" stroke="#0063b4" stroke-width="2"><path d="M5 3h4l2 5-3 2a11 11 0 0 0 6 6l2-3 5 2v4a2 2 0 0 1-2 2A18 18 0 0 1 3 5a2 2 0 0 1 2-2z"/></svg>030 418 2276</span>
    <span><svg width="17" height="13" viewBox="0 0 24 18" fill="none" stroke="#0063b4" stroke-width="2"><rect x="1" y="1" width="22" height="16"/><path d="M1 1l11 9 11-9"/></svg>info@kornbach31.de</span>
  </div>
  <div class="brand"><i></i>Kornbach 31</div>
  <nav class="main-nav">
    <a href="#">Home</a><a href="#">Treppenlifte</a><a href="#">Unternehmen</a><a href="#">Leistungen</a><a href="#" class="btn-contact">Kontakt</a>
  </nav>
</header>

<section class="hero" role="img" aria-label="Foto einer Holztreppe mit Geländer und einem blau gepolsterten Treppenlift-Sitz">
  <h1 class="hero-title">Wir erstellen<br>Treppenlifte in<br>Ihrem Zuhause</h1>
  <p class="hero-sub">Mit unseren Treppenliften finden<br>wir ideale und individuelle Lösungen.</p>
  <svg class="hero-arrow" width="130" height="90" viewBox="0 0 130 90" fill="none" stroke="#0063b4" stroke-width="4" stroke-linecap="round"><path d="M2 12C50-2 95 20 120 80"/><path d="M92 62l28 20 0-32"/></svg>
</section>

<div class="cta-band">
  <h2>KONFIGURIEREN SIE IHREN TREPPENLIFT</h2>
  <p>und erhalten Sie kostenlos Angebote!</p>
</div>

<section class="lift-types">
  <h2>Was für einen Lift suchen Sie?</h2>
  <div class="lift-card" style="left:88px">
    <div class="icon"><svg width="74" height="74" viewBox="0 0 74 74" fill="none" stroke="#0063b4" stroke-width="3"><path d="M8 70h60V30h-14v14h-14v14H26v12"/><circle cx="24" cy="22" r="8"/><path d="M14 34h20M20 34v14M28 34v14M10 12l55 55"/></svg></div>
    <div class="label">Sitzlift</div>
  </div>
  <div class="lift-card is-active" style="left:350px">
    <div class="icon"><svg width="74" height="74" viewBox="0 0 74 74" fill="none" stroke="#fff" stroke-width="3"><path d="M8 70h60V30h-14v14h-14v14H26v12"/><circle cx="22" cy="26" r="7"/><path d="M8 12l55 55M14 40h24"/></svg></div>
    <div class="label">Plattformlift</div>
  </div>
  <div class="lift-card" style="left:611px">
    <div class="icon"><svg width="74" height="74" viewBox="0 0 74 74" fill="none" stroke="#0063b4" stroke-width="3"><rect x="6" y="8" width="36" height="62"/><path d="M42 70h28V40H58v14H46"/><path d="M14 60h20M18 44a6 6 0 0 1 12 0v16H18z"/></svg></div>
    <div class="label">Hublift</div>
  </div>
  <div class="lift-card" style="left:873px">
    <div class="icon" style="font-size:48px;color:var(--blue);font-weight:500">?</div>
    <div class="label">Weiß nicht</div>
  </div>
  <div class="slider-bars"><i class="on"></i><i></i><i></i><i></i><i></i><i></i><i></i></div>
</section>

<div class="about-brand"><i></i>Kornbach 31</div>
<div class="about-col" style="left:263px">
  <p>Lorem ipsum dolor sit amet, consectetur adipiscing elit, sed do eiusmod tempor incididunt ut labore et dolore magna aliqua. Ut enim ad minim veniam, quis nostrud exercitation ullamco laboris nisi ut aliquip ex ea commodo consequat. Duis aute irure dolor in reprehenderit in voluptate velit esse cillum dolore eu fugiat nulla pariatur. Excepteur sint occaecat cupidatat non proident, sunt in culpa qui officia deserunt mollit anim id est laborum.</p>
</div>
<div class="about-col" style="left:614px">
  <p>Sed ut perspiciatis unde omnis iste natus error sit voluptatem accusantium doloremque laudantium, totam rem aperiam, eaque ipsa quae ab illo inventore veritatis et quasi architecto beatae vitae dicta sunt explicabo.</p>
  <p>Nemo enim ipsam voluptatem quia voluptas sit aspernatur aut odit aut fugit, sed quia consequuntur magni dolores eos qui ratione voluptatem sequi nesciunt.</p>
</div>

<div class="photo" style="left:0;top:1600px;width:600px;height:600px;background:linear-gradient(135deg,#d9cdb8,#b9a585 55%,#5a4a3c)" role="img" aria-label="Foto eines älteren Herrn auf einem Treppenlift im Treppenhaus"></div>
<div class="photo" style="left:600px;top:1600px;width:600px;height:600px;background:linear-gradient(135deg,#b48a4e,#9a6f3a 50%,#c9cbd0)" role="img" aria-label="Foto eines Plattformlifts vor einer Natursteinwand"></div>
<div class="feature-box" style="left:600px;top:1600px">
  <h3>Excepteur sint occaecat cupidatat non proident</h3>
  <p>Sed do eiusmod tempor incididunt ut labore et dolore magna aliqua. Quis ipsum suspendisse ultrices gravida. Risus commodo viverra vel facilisis.</p>
</div>
<div class="feature-box" style="left:300px;top:1900px">
  <h3>Ut enim ad minima veniam, quis nostrum</h3>
  <p>Sed do eiusmod tempor incididunt ut labore et dolore magna aliqua. Quis ipsum suspendisse ultrices gravida. Risus commodo viverra vel facilisis.</p>
</div>

<div class="partners">
  <span><i></i>Feldtal</span><span>Norvia</span><span><i></i>Lumeto</span><span>Sarvik</span><span><i></i>Brandholt</span>
</div>
<div class="partner-dots"><i class="on"></i><i></i><i></i></div>

<footer>
  <div class="footer-contact">
    <span><svg width="14" height="18" viewBox="0 0 14 18" fill="none" stroke="#333" stroke-width="1.5"><path d="M7 17s6-6 6-10A6 6 0 0 0 1 7c0 4 6 10 6 10z"/><circle cx="7" cy="7" r="2"/></svg>Lindenweg 14, 54321 Beispielfeld</span>
    <span><svg width="16" height="16" viewBox="0 0 24 24" fill="none" stroke="#333" stroke-width="1.8"><path d="M5 3h4l2 5-3 2a11 11 0 0 0 6 6l2-3 5 2v4a2 2 0 0 1-2 2A18 18 0 0 1 3 5a2 2 0 0 1 2-2z"/></svg>030 418 2276</span>
    <span><svg width="17" height="13" viewBox="0 0 24 18" fill="none" stroke="#333" stroke-width="1.8"><rect x="1" y="1" width="22" height="16"/><path d="M1 1l11 9 11-9"/></svg>info@kornbach31.de</span>
  </div>
  <div class="footer-bar">
    <div class="copy">©2022 Kornbach 31</div>
    <div class="legal"><span>Impressum</span><span>Datenschutz</span></div>
  </div>
</footer>

</body>
</html>
```